Spice Mix Label Bottle Branding - Health and Weight Loss Mixes

The company is called ZestRow Spice Mix's. We've created 5 spice mixes using ingredients that promote health and weight loss. We already have a logo but now we need labels for our bottles. We would like to see designs that have the feel of health supplements (see attached examples)

We would like a different colour featured with each of our flavours.

Our flavours are:
-Golden Chai (Yellow)
-Mild Curry (Orange)
-Coffee Rub (brown)
-Garlic Oregano (Green)
-Taco (Blue)

Thank you!

Target Market(s)

Ages 22-35. Men and Female. Trendy, Hipster.

Industry/Entity Type

Food Production

Font styles to use
Sans Serif

Colors
f37122
0655a3
0692cd
9bcb3c
fbee3f

Requirements
Must have
• A different featured colour for each flavour.
• The ZestRow Spices Logo (attached)
• The slogan: "Weight Loss Ingredients"
• -Golden Chai (Yellow)
• -Mild Curry (Orange)
• -Coffee Rub (brown)
• -Garlic Oregano (Green)
• -Taco (Blue)
• Text Files attached.
Nice to have
• A black label with a featured colour for each of the spice mice flavours.
• 'No Salt added'

```html
<!DOCTYPE html>
<html lang="en">
<head>
<meta charset="utf-8">
<title>ZestRow Spices – Flavour Labels</title>
<link rel="stylesheet" href="https://fonts.googleapis.com/css2?family=Oswald:wght@500;700&family=Roboto+Slab:wght@800&family=Roboto+Condensed:ital,wght@0,400;1,700&display=swap">
<style>
  :root {
    --page-bg: #f4f5f7;
    --label-bg: #121212;
    --label-edge: #1c1c1c;
    --text-light: #e6e6e6;
    --text-muted: #9a9a9a;
    --chai: #c8913b;
    --chai-deep: #8a5a1c;
    --garlic: #8cc640;
    --garlic-deep: #4f7d1f;
    --taco: #4277b8;
    --taco-deep: #1f4475;
    --ink: #111111;
  }
  * { box-sizing: border-box; margin: 0; padding: 0; }
  html, body { width: 1200px; height: 1050px; overflow: hidden; background: var(--page-bg); }
  .label-set {
    position: relative; width: 1200px; height: 1050px;
    display: flex; justify-content: center; align-items: center; gap: 45px;
  }
  .label {
    position: relative; width: 340px; height: 620px;
    background: var(--label-bg);
    border: 1px solid var(--label-edge);
    display: flex; flex-direction: column; align-items: center;
    overflow: hidden;
  }
  .label--chai { --accent: var(--chai); --accent-deep: var(--chai-deep); }
  .label--garlic { --accent: var(--garlic); --accent-deep: var(--garlic-deep); }
  .label--taco { --accent: var(--taco); --accent-deep: var(--taco-deep); }

  .label__figure {
    position: absolute; left: 20px; right: 20px; top: 60px; bottom: 120px;
    border-radius: 120px 120px 60px 60px;
    background: radial-gradient(ellipse at 50% 45%, #2a2a2a 0%, #1a1a1a 55%, rgba(18,18,18,0) 75%);
  }
  .brand { position: relative; margin-top: 70px; text-align: center; }
  .brand__mark {
    display: inline-block; width: 12px; height: 12px; border-radius: 50%;
    background: var(--accent); margin-bottom: 8px;
  }
  .brand__name {
    font-family: "Oswald", sans-serif; font-weight: 700; font-size: 48px;
    line-height: 1; color: var(--text-light); letter-spacing: 0.5px;
  }
  .brand__tagline {
    margin-top: 8px; padding-top: 4px;
    font-family: "Roboto Condensed", sans-serif; font-size: 10px; font-weight: 400;
    letter-spacing: 0.6px; color: var(--text-light);
    border-top: 2px solid var(--accent); border-bottom: 1px solid var(--text-muted);
    padding-bottom: 3px;
  }
  .claim { position: relative; margin-top: 92px; text-align: center; color: var(--text-muted); }
  .claim__lead {
    font-family: "Oswald", sans-serif; font-weight: 500; font-size: 12px; letter-spacing: 1px;
  }
  .claim__title {
    font-family: "Roboto Slab", sans-serif; font-weight: 800; font-size: 17px; letter-spacing: 1.5px;
    color: #b5b5b5;
  }
  .claim__copy {
    position: relative; width: 230px; margin-top: 16px; text-align: center;
    font-family: "Roboto Condensed", sans-serif; font-size: 8px; line-height: 1.3; color: #c8c8c8;
  }
  .flavour { position: relative; margin-top: 12px; width: 270px; height: 78px; }
  .flavour svg { position: absolute; inset: 0; width: 100%; height: 100%; }
  .flavour__name {
    position: absolute; inset: 0; display: flex; align-items: center; justify-content: center;
    font-family: "Oswald", sans-serif; font-weight: 700; font-size: 30px; letter-spacing: 0.5px;
    color: var(--ink);
  }
  .flavour__name--small { font-size: 26px; }
  .no-salt {
    position: relative; margin-top: 10px; padding: 1px 14px; border-radius: 9px;
    background: var(--accent);
    font-family: "Roboto Condensed", sans-serif; font-style: italic; font-weight: 700; font-size: 12px;
    color: var(--ink);
  }
</style>
</head>
<body>
<main class="label-set">

  <article class="label label--chai">
    <div class="label__figure" role="img" aria-label="Faint athletic torso illustration"></div>
    <header class="brand">
      <span class="brand__mark"></span>
      <div class="brand__name">ZestRow Spices</div>
      <div class="brand__tagline">WEIGHT LOSS SEASONINGS</div>
    </header>
    <section class="claim">
      <div class="claim__lead">★ ★ ★ PERFECT FOR ★ ★ ★</div>
      <div class="claim__title">WEIGHTLOSS</div>
    </section>
    <p class="claim__copy">Rich in antioxidants flush out toxins, free of synthetic ingredients to flush out harmful toxins from body, Supports Weight Loss through reduced bloating, Healthy digestion increases metabolism.</p>
    <div class="flavour">
      <svg viewBox="0 0 270 78" aria-hidden="true">
        <polygon points="0,12 22,12 22,2 248,2 248,12 270,12 256,39 270,66 248,66 248,76 22,76 22,66 0,66 14,39" fill="var(--accent)"/>
        <polygon points="8,18 28,18 28,8 242,8 242,18 262,18 250,39 262,60 242,60 242,70 28,70 28,60 8,60 20,39" fill="none" stroke="#f1e3c4" stroke-width="1.5"/>
      </svg>
      <div class="flavour__name">GOLDEN CHAI</div>
    </div>
    <div class="no-salt">No Salt added</div>
  </article>

  <article class="label label--garlic">
    <div class="label__figure" role="img" aria-label="Faint athletic torso illustration"></div>
    <header class="brand">
      <span class="brand__mark"></span>
      <div class="brand__name">ZestRow Spices</div>
      <div class="brand__tagline">WEIGHT LOSS SEASONINGS</div>
    </header>
    <section class="claim">
      <div class="claim__lead">★ ★ ★ PERFECT FOR ★ ★ ★</div>
      <div class="claim__title">WEIGHTLOSS</div>
    </section>
    <p class="claim__copy">Rich in antioxidants flush out toxins, free of synthetic ingredients to flush out harmful toxins from body, Supports Weight Loss through reduced bloating, Healthy digestion increases metabolism.</p>
    <div class="flavour">
      <svg viewBox="0 0 270 78" aria-hidden="true">
        <polygon points="0,12 22,12 22,2 248,2 248,12 270,12 256,39 270,66 248,66 248,76 22,76 22,66 0,66 14,39" fill="var(--accent)"/>
        <polygon points="8,18 28,18 28,8 242,8 242,18 262,18 250,39 262,60 242,60 242,70 28,70 28,60 8,60 20,39" fill="none" stroke="#e4f2cf" stroke-width="1.5"/>
      </svg>
      <div class="flavour__name flavour__name--small">GARLIC OREGANO</div>
    </div>
    <div class="no-salt">No Salt added</div>
  </article>

  <article class="label label--taco">
    <div class="label__figure" role="img" aria-label="Faint athletic torso illustration"></div>
    <header class="brand">
      <span class="brand__mark"></span>
      <div class="brand__name">ZestRow Spices</div>
      <div class="brand__tagline">WEIGHT LOSS SEASONINGS</div>
    </header>
    <section class="claim">
      <div class="claim__lead">★ ★ ★ PERFECT FOR ★ ★ ★</div>
      <div class="claim__title">WEIGHTLOSS</div>
    </section>
    <p class="claim__copy">Rich in antioxidants flush out toxins, free of synthetic ingredients to flush out harmful toxins from body, Supports Weight Loss through reduced bloating, Healthy digestion increases metabolism.</p>
    <div class="flavour">
      <svg viewBox="0 0 270 78" aria-hidden="true">
        <polygon points="0,12 22,12 22,2 248,2 248,12 270,12 256,39 270,66 248,66 248,76 22,76 22,66 0,66 14,39" fill="var(--accent)"/>
        <polygon points="8,18 28,18 28,8 242,8 242,18 262,18 250,39 262,60 242,60 242,70 28,70 28,60 8,60 20,39" fill="none" stroke="#d3e1f3" stroke-width="1.5"/>
      </svg>
      <div class="flavour__name">TACO</div>
    </div>
    <div class="no-salt">No Salt added</div>
  </article>

</main>
</body>
</html>
```